NEW Modern Sleek Business Card for VR Language Startup

Our startup is using VR to lead the next wave of world language education. We need a two-sided business card that introduces the larger organization (Quorvel Language Inc) and our contact info on one side and shows the product, Lumidrasca, on the other side.

Side 1 (contact info)= Quorvel Logo and Contact info (name, title, phone, email)

Side 2 (product)= Lumidrasc logo, text, and website
Text= Culturally Immersive Language Learning Games
Website= www.lumidrasc.example

Target Market(s)

Education, Technology

Contact Information for Business Card

Contact info will be updated upon approval of the design. For now, put this as a placeholder.

Perry Hollins
Founder & CEO
phollins@mailtrove.example
(555)-014-2736

Font styles to use
Other font styles liked:
• Gibson and Century Gothic are the brand fonts

Requirements
Nice to have
• I would love to see cohesion between the design and colors of the two logos. I have attached a few business card designs that I like, so you can get a feel for my preferred style.

```html
<!DOCTYPE html>
<html lang="en">
<head>
<meta charset="utf-8">
<title>Quorvel Language – Business Card</title>
<link rel="stylesheet" href="https://fonts.googleapis.com/css2?family=Lato:wght@400;700&family=Montserrat:wght@600;700&display=swap">
<style>
  :root {
    --bg: #6e6e6e;
    --card: #fbfbfb;
    --ink: #1c1c1c;
    --ink-soft: #4a4a4a;
    --red: #ee2a4a;
    --orange: #f59a1f;
    --cyan: #2fe3e6;
    --blue: #4f6ff0;
    --violet: #8a5be0;
    --purple: #6a4fd6;
    --magenta: #c04fc8;
  }
  * { box-sizing: border-box; margin: 0; padding: 0; }
  html, body { width: 1200px; height: 1056px; overflow: hidden; }
  body {
    background: var(--bg);
    font-family: "Lato", sans-serif;
    position: relative;
  }
  .card {
    position: absolute;
    left: 160px;
    width: 880px;
    height: 440px;
    background: var(--card);
    overflow: hidden;
    box-shadow: 0 10px 26px rgba(0,0,0,.35);
  }
  .card--contact { top: 56px; }
  .card--product { top: 560px; }
  .card__art { position: absolute; inset: 0; width: 100%; height: 100%; }

  .brand {
    position: absolute;
    display: flex;
    flex-direction: column;
    align-items: center;
    gap: 22px;
    font-family: "Montserrat", sans-serif;
    font-weight: 700;
  }
  .brand__dot { width: 120px; height: 120px; border-radius: 50%; }
  .brand--company { left: 60px; top: 92px; width: 340px; }
  .brand--company .brand__dot { background: var(--red); }
  .brand--company .brand__name { font-size: 58px; letter-spacing: 6px; color: var(--ink); }

  .contact {
    position: absolute;
    right: 58px;
    top: 150px;
    text-align: right;
  }
  .contact__name { font-size: 36px; font-weight: 700; color: var(--red); line-height: 1.1; }
  .contact__title { font-size: 21px; color: var(--ink); margin-top: 4px; }
  .contact__rule {
    height: 3px; width: 330px; margin: 12px 0 12px auto;
    background: linear-gradient(90deg, var(--orange), var(--red), var(--violet), var(--cyan));
  }
  .contact__line { font-size: 22px; color: var(--ink); display: flex; justify-content: flex-end; align-items: center; gap: 10px; line-height: 1.5; }
  .contact__icon { width: 18px; height: 18px; flex: none; }

  .brand--product { left: 70px; top: 100px; width: 360px; }
  .brand--product .brand__dot { background: var(--purple); }
  .brand--product .brand__name { font-size: 50px; color: var(--purple); }
  .product__site { font-family: "Lato", sans-serif; font-weight: 400; font-size: 24px; color: var(--purple); margin-top: -10px; letter-spacing: .5px; }

  .tagline {
    position: absolute;
    left: 540px; right: 40px; top: 96px;
    font-family: "Montserrat", sans-serif;
    font-weight: 700;
    font-size: 40px;
    line-height: 1.2;
    letter-spacing: 1px;
    color: #ffffff;
    text-align: center;
    text-transform: uppercase;
  }
</style>
</head>
<body>

<section class="card card--contact">
  <svg class="card__art" viewBox="0 0 880 440" aria-hidden="true">
    <defs>
      <linearGradient id="wedgeCool" x1="0" y1="0" x2="0" y2="1">
        <stop offset="0" stop-color="#2fe3e6"/>
        <stop offset="1" stop-color="#4f6ff0"/>
      </linearGradient>
      <linearGradient id="wedgeWarm" x1="0" y1="0" x2="0" y2="1">
        <stop offset="0" stop-color="#f59a1f"/>
        <stop offset=".35" stop-color="#ee2a4a"/>
        <stop offset=".7" stop-color="#b04fd0"/>
        <stop offset="1" stop-color="#4f6ff0"/>
      </linearGradient>
    </defs>
    <polygon points="455,0 498,0 512,440" fill="url(#wedgeCool)"/>
    <polygon points="498,0 540,0 512,440" fill="url(#wedgeWarm)"/>
  </svg>

  <div class="brand brand--company">
    <span class="brand__dot"></span>
    <span class="brand__name">Quorvel</span>
  </div>

  <div class="contact">
    <p class="contact__name">Perry Hollins</p>
    <p class="contact__title">Founder &amp; CEO</p>
    <div class="contact__rule"></div>
    <p class="contact__line">(555)-014-2736
      <svg class="contact__icon" viewBox="0 0 24 24" aria-hidden="true"><path fill="#ee2a4a" d="M6.6 10.8a15.1 15.1 0 0 0 6.6 6.6l2.2-2.2c.3-.3.7-.4 1-.2 1.1.4 2.3.6 3.6.6.6 0 1 .4 1 1V20c0 .6-.4 1-1 1A17 17 0 0 1 3 4c0-.6.4-1 1-1h3.5c.6 0 1 .4 1 1 0 1.3.2 2.5.6 3.6.1.3 0 .7-.2 1z"/></svg>
    </p>
    <p class="contact__line">phollins@mailtrove.example
      <svg class="contact__icon" viewBox="0 0 24 24" aria-hidden="true"><path fill="#ee2a4a" d="M2 5h20v14H2z"/><path fill="none" stroke="#fff" stroke-width="1.8" d="M2.5 5.5 12 13l9.5-7.5"/></svg>
    </p>
  </div>
</section>

<section class="card card--product">
  <svg class="card__art" viewBox="0 0 880 440" role="img" aria-label="Soft cyan to violet faceted backdrop panel">
    <defs>
      <linearGradient id="panelFill" x1="0" y1="0" x2="1" y2="1">
        <stop offset="0" stop-color="#3fd8ea"/>
        <stop offset=".35" stop-color="#8a7ef0"/>
        <stop offset=".7" stop-color="#a45ed8"/>
        <stop offset="1" stop-color="#5a6ff0"/>
      </linearGradient>
      <linearGradient id="panelEdge" x1="0" y1="0" x2="0" y2="1">
        <stop offset="0" stop-color="#2fe3e6"/>
        <stop offset="1" stop-color="#4f6ff0"/>
      </linearGradient>
    </defs>
    <polygon points="505,0 880,0 880,440 485,440" fill="url(#panelFill)"/>
    <polygon points="505,0 545,0 500,300 485,440" fill="url(#panelEdge)"/>
    <polygon points="485,440 530,440 600,440 500,330" fill="#2fe3e6" opacity=".8"/>
  </svg>

  <div class="brand brand--product">
    <span class="brand__dot"></span>
    <span class="brand__name">Lumidrasc</span>
    <span class="product__site">www.lumidrasc.example</span>
  </div>

  <p class="tagline">Culturally<br>Immersive<br>Language<br>Learning<br>Games</p>
</section>

</body>
</html>
```